Brochure Design Project

We need a nice, warm, friendly Brochure for First Home Buyer in Australia.
It is actually a 32 pages Handbook. It has the Guide, what to aware and the process for first time home buyer.
Content will be provided.
And wish to have a flow with our letter head design or flyer design attached.
Reason: I need to show a example
Reason: We are waiting for more designers' submission.
Target Market(s)
First Home Buyer
Look and feel

```html
<!DOCTYPE html>
<html lang="en">
<head>
<meta charset="utf-8">
<title>First Home Owner Handbook – Spread</title>
<link rel="stylesheet" href="https://fonts.googleapis.com/css2?family=Crimson+Text:ital,wght@0,400;0,600;0,700;1,400;1,600;1,700&family=Open+Sans:wght@700&display=swap">
<style>
:root{
  --gold-top:#e2cd8c;
  --gold-bottom:#c9b46b;
  --sage-band:#bcc39a;
  --page-left-top:#d3dcc6;
  --page-left-bottom:#f2f4ec;
  --page-right-top:#d8e0cc;
  --page-right-bottom:#fbfbf8;
  --ink:#1c2c14;
  --ink-soft:#2c3a22;
  --olive:#6f7f3a;
  --box:#bbc396;
  --leaf:#7a9a1e;
  --leaf-light:#b8d24a;
}
*{margin:0;padding:0;box-sizing:border-box}
html,body{width:1200px;height:906px;overflow:hidden;background:#fff}
body{font-family:"Crimson Text",Georgia,serif;color:var(--ink);position:relative}

.page{position:absolute;top:0;height:906px;overflow:hidden}
.page--left{left:0;width:600px;background:linear-gradient(180deg,var(--page-left-top),var(--page-left-bottom))}
.page--right{left:600px;width:600px;background:linear-gradient(180deg,var(--page-right-top),var(--page-right-bottom))}

.running-head{position:absolute;top:0;left:0;right:0;height:61px;background:linear-gradient(180deg,var(--gold-top),var(--gold-bottom));display:flex;align-items:center;justify-content:space-between;padding:0 63px;font-weight:700;font-size:17px;color:var(--ink)}
.page--right .running-head{padding:0 60px 0 48px}
.running-head .book-title{font-style:italic;font-weight:400;font-size:18px}

.running-foot{position:absolute;bottom:0;left:0;right:0;height:63px;background:var(--sage-band);display:flex;align-items:center;font-style:italic;font-size:13.5px;color:var(--ink-soft)}
.folio{font-family:"Open Sans",Arial,sans-serif;font-style:normal;font-weight:700;font-size:17px;color:#5b6240}
.page--left .running-foot{padding-left:44px}
.page--left .folio{margin-right:30px}
.page--right .running-foot{justify-content:flex-end;padding-right:44px}
.page--right .web{margin-right:200px;font-size:14.5px}

.cover-title{position:absolute;top:120px;left:0;width:556px;text-align:center;font-style:italic;font-weight:700;font-size:25px;color:var(--ink)}
.brand-mark{position:absolute;left:185px;top:215px;width:210px;height:210px;border-radius:50%;background:radial-gradient(circle at 40% 35%,var(--leaf-light),var(--leaf) 70%)}
.brand-name{position:absolute;top:468px;left:0;width:556px;text-align:center;font-weight:700;font-size:18px;letter-spacing:.3px}
.brand-tagline{position:absolute;top:494px;left:0;width:556px;text-align:center;font-weight:700;font-size:15px}

.contact-card{position:absolute;left:65px;top:577px;width:482px;height:216px;background:var(--box);border-radius:32px}
.contact-card h2{position:absolute;top:10px;left:0;width:100%;text-align:center;font-family:"Open Sans",Arial,sans-serif;font-size:27px;color:var(--olive);text-decoration:underline;text-underline-offset:3px;letter-spacing:.5px}
.contact-lines{position:absolute;top:52px;left:0;width:100%;text-align:center;font-size:15px;line-height:20px}
.contact-lines .gap{display:inline-block;width:60px}
.office{position:absolute;top:116px;font-size:15px;line-height:20px;font-style:normal}
.office--sydney{left:20px}
.office--branch{left:254px}

.toc-title{position:absolute;top:74px;left:0;width:600px;text-align:center;font-variant:small-caps;font-weight:700;font-size:20px;letter-spacing:1.5px}
.toc-rule{position:absolute;top:104px;left:49px;width:489px;height:1px;background:#4a5238}
.toc{position:absolute;left:49px;width:489px}
.toc h3{font-variant:small-caps;font-weight:700;font-size:14px;height:20px;line-height:20px;letter-spacing:.4px}
.toc ul{list-style:none}
.toc li{display:flex;align-items:baseline;height:19.8px;font-size:14.5px;padding-left:10px}
.toc li svg{width:12px;height:10px;margin-right:12px;flex:none;align-self:center}
.toc li .dots{flex:1;border-bottom:1.5px dotted #333;margin:0 2px 4px 6px}
.toc--upfront{top:121px}
.toc--finance{top:269px}
.toc--purchase{top:396px}
.toc--after{top:545px}

.notice{position:absolute;top:640px;left:49px;width:489px}
.notice h4{text-align:center;font-variant:small-caps;font-weight:700;font-size:13.5px;letter-spacing:.6px;margin-bottom:6px}
.notice p{font-size:11.2px;line-height:17.5px;text-align:justify}
</style>
</head>
<body>

<section class="page page--left">
  <header class="running-head"><span>KEYSTONE HOME LOANS</span></header>

  <h1 class="cover-title">First Home Owner Hand book</h1>
  <div class="brand-mark" role="img" aria-label="Keystone Home Loans brand mark"></div>
  <p class="brand-name">KEYSTONE HOME LOANS</p>
  <p class="brand-tagline">BUILT ON TRUST</p>

  <div class="contact-card">
    <h2>CONTACT US</h2>
    <p class="contact-lines">Tel: 02 8000 1234,<span class="gap"></span>Fax: 02 9000 5678<br>Email: info@keystonehomeloans.com.au</p>
    <address class="office office--sydney">Sydney Office<br>Suite 210, Harbour Building<br>120 Clarence Street<br>Sydney NSW 2000</address>
    <address class="office office--branch">Parramatta Office<br>Suite 305, Riverside Centre<br>45 Station Road<br>Parramatta NSW 2150</address>
  </div>

  <footer class="running-foot"><span class="folio">2</span><span>Tel: 02 8000 1234&nbsp; Fax: 02 9000 5678&nbsp; Email: info@keystonehomeloans.com.au</span></footer>
</section>

<section class="page page--right">
  <header class="running-head"><span>BUILT ON TRUST</span><span class="book-title">First Home Owner Handbook</span></header>

  <h2 class="toc-title">Table of Contents</h2>
  <div class="toc-rule"></div>

  <div class="toc toc--upfront">
    <h3>Upfront Considerations</h3>
    <ul>
      <li><svg viewBox="0 0 12 10"><path d="M1 5 L8 1 L11 5 L8 9 Z" fill="#2c3a22"/></svg>Budget plan<span class="dots"></span>1</li>
      <li><svg viewBox="0 0 12 10"><path d="M1 5 L8 1 L11 5 L8 9 Z" fill="#2c3a22"/></svg>Borrow capacity<span class="dots"></span>1</li>
      <li><svg viewBox="0 0 12 10"><path d="M1 5 L8 1 L11 5 L8 9 Z" fill="#2c3a22"/></svg>Required deposit<span class="dots"></span>1</li>
      <li><svg viewBox="0 0 12 10"><path d="M1 5 L8 1 L11 5 L8 9 Z" fill="#2c3a22"/></svg>First home owner grant<span class="dots"></span>2</li>
      <li><svg viewBox="0 0 12 10"><path d="M1 5 L8 1 L11 5 L8 9 Z" fill="#2c3a22"/></svg>First home saver account<span class="dots"></span>5</li>
      <li><svg viewBox="0 0 12 10"><path d="M1 5 L8 1 L11 5 L8 9 Z" fill="#2c3a22"/></svg>Which comes first, finance or property<span class="dots"></span>6</li>
    </ul>
  </div>

  <div class="toc toc--finance">
    <h3>Considerations When Obtaining Finance</h3>
    <ul>
      <li><svg viewBox="0 0 12 10"><path d="M1 5 L8 1 L11 5 L8 9 Z" fill="#2c3a22"/></svg>Choosing a mortgage broker<span class="dots"></span>8</li>
      <li><svg viewBox="0 0 12 10"><path d="M1 5 L8 1 L11 5 L8 9 Z" fill="#2c3a22"/></svg>Loan types<span class="dots"></span>10</li>
      <li><svg viewBox="0 0 12 10"><path d="M1 5 L8 1 L11 5 L8 9 Z" fill="#2c3a22"/></svg>Loan features<span class="dots"></span>17</li>
      <li><svg viewBox="0 0 12 10"><path d="M1 5 L8 1 L11 5 L8 9 Z" fill="#2c3a22"/></svg>Commonly used accounts<span class="dots"></span>19</li>
      <li><svg viewBox="0 0 12 10"><path d="M1 5 L8 1 L11 5 L8 9 Z" fill="#2c3a22"/></svg>Documents required<span class="dots"></span>21</li>
    </ul>
  </div>

  <div class="toc toc--purchase">
    <h3>Considerations When Purchasing A Property</h3>
    <ul>
      <li><svg viewBox="0 0 12 10"><path d="M1 5 L8 1 L11 5 L8 9 Z" fill="#2c3a22"/></svg>Associated costs<span class="dots"></span>22</li>
      <li><svg viewBox="0 0 12 10"><path d="M1 5 L8 1 L11 5 L8 9 Z" fill="#2c3a22"/></svg>Home inspection<span class="dots"></span>24</li>
      <li><svg viewBox="0 0 12 10"><path d="M1 5 L8 1 L11 5 L8 9 Z" fill="#2c3a22"/></svg>Loan process<span class="dots"></span>25</li>
      <li><svg viewBox="0 0 12 10"><path d="M1 5 L8 1 L11 5 L8 9 Z" fill="#2c3a22"/></svg>Understand a contract of sale<span class="dots"></span>26</li>
      <li><svg viewBox="0 0 12 10"><path d="M1 5 L8 1 L11 5 L8 9 Z" fill="#2c3a22"/></svg>The general buying process<span class="dots"></span>28</li>
      <li><svg viewBox="0 0 12 10"><path d="M1 5 L8 1 L11 5 L8 9 Z" fill="#2c3a22"/></svg>The 7 mistakes first home buyers can avoid<span class="dots"></span>30</li>
    </ul>
  </div>

  <div class="toc toc--after">
    <h3>Considerations After Settlement</h3>
    <ul>
      <li><svg viewBox="0 0 12 10"><path d="M1 5 L8 1 L11 5 L8 9 Z" fill="#2c3a22"/></svg>Moving<span class="dots"></span>31</li>
      <li><svg viewBox="0 0 12 10"><path d="M1 5 L8 1 L11 5 L8 9 Z" fill="#2c3a22"/></svg>How to pay off the mortgage<span class="dots"></span>32</li>
    </ul>
  </div>

  <div class="notice">
    <h4>Polite notice</h4>
    <p>Any comments and statements that are published herein are directly from the editorial contributors and should not be treated as a recommendation that a particular course of action is suitable for you. The opinions that have been expressed do not necessarily represent the viewpoints of the publisher and your use of any materials contained in this booklet is exclusively at your own risk. Although Keystone has taken all reasonable efforts and care to ensure that the information is correct at the time of publication, the accuracy and reliability of the published information cannot be guaranteed. Hence, Keystone will not assume any responsibility for the accuracy, completeness or authenticity of any published information and is not liable to you or any third party for any losses or damages suffered directly or indirectly through your use of the information. Copyright Keystone Finance and Property 2010</p>
  </div>

  <footer class="running-foot"><span class="web">www.keystonehomeloans.com.au</span><span class="folio">3</span></footer>
</section>

</body>
</html>
```